Ferncastle Holdings - stationery for luxury, exclusive property investment company

We need stationery (letterhead, folder, compliments slip and envelope) and business cards which will reflect our luxury brand.

I have attached some design examples that we like.

We are an investment company which buys property to provide accommodation for corporate customers.

The design of the stationery needs to be be simple, refined, understated, luxury and very tasteful.

The design should communicate luxury and exclusivity, without being ostentatious.

Logo files are attached

Please can designers re-read the brief, and make sure the logo is in gold on either on a navy or white background.

Target Market(s)

Wealthy customers

Contact Information for Business Card

Helen Travers-Booth
Director
Ferncastle Holdings Limited
email: helen@ferncastleholdings.co.uk
mob: 07712645930

Font styles to use
Serif

Colors

Designer to choose colors to be used in the design.

Requirements
Must have
• The logo must be gold on either a white or navy background as per the attached logos.
• The stationery MUST have the following information:
• Ferncastle Holdings Limited
• The Willows
• Ashby Rise
• Ashby
• GL52 7TN
• Company Number: 20418736 (Registered in England and Wales)
• The letterhead must also have the two attached logos for the PLG and the PLG accreditation scheme. They do not need to be large.
Nice to have
• A watermark, navy banding either top or bottom.
Should not have
• Anything that looks budget.

```html
<!DOCTYPE html>
<html lang="en">
<head>
<meta charset="utf-8">
<title>Ferncastle Holdings – Envelope and Compliments Slip</title>
<link rel="stylesheet" href="https://fonts.googleapis.com/css2?family=Jost:wght@300;400&display=swap">
<style>
  :root {
    --navy: #020338;
    --gold: #b8923f;
    --sheet-edge: #cfcfcf;
    --label-grey: #c4c4c4;
    --window-line: #111111;
    --paper: #ffffff;
  }
  * { margin: 0; padding: 0; box-sizing: border-box; }
  html, body {
    width: 1048px;
    height: 1200px;
    overflow: hidden;
    background: var(--paper);
    font-family: "Jost", sans-serif;
  }
  .canvas { position: relative; width: 1048px; height: 1200px; }

  .sheet {
    position: absolute;
    left: 0;
    width: 1048px;
    border: 1px solid var(--sheet-edge);
    background: var(--paper);
    overflow: hidden;
  }
  .envelope { top: 0; height: 504px; }
  .comp-slip { top: 616px; height: 503px; }

  .brand-name {
    position: absolute;
    color: var(--gold);
    font-weight: 400;
    text-transform: uppercase;
    text-align: center;
    line-height: 1.15;
    letter-spacing: 0.14em;
  }
  .envelope .brand-name { left: 100px; top: 118px; width: 240px; font-size: 25px; }
  .comp-slip .brand-name { left: 56px; top: 106px; width: 300px; font-size: 31px; }

  .address-window {
    position: absolute;
    left: 104px;
    top: 216px;
    width: 410px;
    height: 190px;
    border: 1.5px solid var(--window-line);
    border-radius: 8px;
  }

  .navy-band { position: absolute; background: var(--navy); }
  .envelope .navy-band { left: 954px; top: 252px; width: 94px; height: 252px; }
  .comp-slip .navy-band { left: 917px; top: 117px; width: 92px; height: 386px; }

  .compliments {
    position: absolute;
    left: 46px;
    bottom: 36px;
    transform-origin: left bottom;
    transform: rotate(-90deg) translateY(0);
    white-space: nowrap;
    color: var(--gold);
    font-weight: 300;
    font-size: 40px;
    letter-spacing: 0.01em;
    line-height: 1;
  }

  .address-line {
    position: absolute;
    left: 72px;
    top: 425px;
    color: var(--gold);
    font-weight: 300;
    font-size: 19px;
    white-space: nowrap;
  }
  .address-line .sep { margin: 0 4px; }

  .sheet-label {
    position: absolute;
    left: 0;
    width: 1068px;
    text-align: center;
    color: var(--label-grey);
    font-weight: 300;
    font-size: 40px;
  }
  .envelope-label { top: 514px; }
  .comp-slip-label { top: 1150px; }
</style>
</head>
<body>
<main class="canvas">
  <section class="sheet envelope" aria-label="Envelope">
    <div class="brand-name">Ferncastle<br>Holdings</div>
    <div class="address-window"></div>
    <div class="navy-band"></div>
  </section>
  <p class="sheet-label envelope-label">Envelope</p>

  <section class="sheet comp-slip" aria-label="Compliments slip">
    <div class="brand-name">Ferncastle<br>Holdings</div>
    <p class="address-line">Ferncastle Holdings Limited<span class="sep">•</span>The Willows<span class="sep">•</span>Ashby Rise<span class="sep">•</span>Ashby<span class="sep">•</span>GL52 7TN</p>
    <div class="navy-band">
      <span class="compliments">With Compliments</span>
    </div>
  </section>
  <p class="sheet-label comp-slip-label">Comp Slip</p>
</main>
</body>
</html>
```